Rack Card for Charter Sail Boat business in SF Bay

We are in need of a rack card design to highlight the business to tourists and locals. 2 sided card 3.86" x 8.39" (full bleed)

We are looking for visually appleaing designs on the front and back but a little more detail on the back.

Use the info provided (text and info) on the website to include the 3 key services (Quick, 1/2 day, fullday) and aspects of the boat, location and other key info for customers (not prices). DO NOT INCLUDE ALL THIS TEXT please pick the elements you would like to fit your design and inform the customer as you would like about the business.

I can also provide photos directly from the video if you think those would fit your design. If video doesn't work on this upload you can view it at the website or facebook page (www.fb.com/tidewrenllc)

Now included a few video pictures in files for your use

Target Market(s)

Tourists and locals to san francisco east bay. 25 - 55 years old. Men and women.

Industry/Entity Type

Entertainment

Colors
0455a3
ec1f27
f3f1f8

Requirements
Must have
• Highlight services, key contact information (email, phone, website site), Visual impact
• 2-sided card - 3.86" x 8.39" (98 x 213 mm)
Nice to have
• facebook link, electric engine(green),

```html
<!DOCTYPE html>
<html lang="en">
<head>
<meta charset="utf-8">
<title>Tidewren Rack Card</title>
<link rel="stylesheet" href="https://fonts.googleapis.com/css2?family=Arimo:wght@400;700&family=Noto+Serif:wght@400;700&family=Oswald:wght@500;700&display=swap">
<style>
:root{
  --blue:#0455a3;
  --red:#ec1f27;
  --paper:#f3f1f8;
  --white:#ffffff;
  --ink:#1d1d1f;
  --gold:#ffd21f;
  --stage:#dcdcde;
  --water:#cfe2f1;
}
*{box-sizing:border-box;margin:0;padding:0}
html,body{width:1200px;height:1200px;overflow:hidden;background:var(--stage)}
body{position:relative;font-family:"Arimo",Arial,sans-serif;color:var(--ink)}
.card{position:absolute;top:100px;width:460px;height:1000px;background:var(--white);overflow:hidden;box-shadow:0 6px 18px rgba(0,0,0,.18)}
.card--front{left:110px}
.card--back{left:630px}
.abs{position:absolute}
.photo{position:absolute}
.photo--hero{left:0;top:0;width:460px;height:340px;background:linear-gradient(180deg,#8fb3d6 0%,#f0c27a 34%,#6d8fae 46%,#2c557c 70%,#1c3d5e 100%)}
.brand{position:absolute;left:228px;top:28px;display:flex;align-items:center;gap:10px}
.brand__dot{width:26px;height:26px;border-radius:50%;background:var(--blue)}
.brand__name{font-family:"Noto Serif",Georgia,serif;font-size:38px;font-weight:400;color:var(--blue);line-height:1}
.photo--circle{border-radius:50%;border:6px solid var(--white);box-shadow:0 2px 8px rgba(0,0,0,.25);z-index:3}
.photo--sails{left:282px;top:262px;width:190px;height:190px;background:radial-gradient(circle at 40% 35%,#ffffff 0%,#c9d6e4 30%,#3f7fc0 60%,#1c4f8c 100%)}
.photo--moored{left:8px;top:500px;width:170px;height:170px;background:linear-gradient(180deg,#7fb0dc 0%,#a7c8e2 45%,#2b3a55 62%,#6e7d8e 100%)}
.headline{position:absolute;left:26px;top:376px;width:250px;font-family:"Noto Serif",Georgia,serif;font-size:21px;line-height:1.18;color:var(--white);z-index:2}
.section h3{font-family:"Noto Serif",Georgia,serif;font-weight:700;font-size:20px;line-height:1.1;margin-bottom:3px}
.section p{font-size:11.5px;line-height:1.24}
.section--modern{left:200px;top:518px;width:244px}
.section--modern h3{color:var(--red)}
.section--entertain{left:214px;top:652px;width:232px}
.section--entertain h3{color:var(--blue)}
.section--safe{left:16px;top:686px;width:190px}
.section--safe h3{color:var(--red)}
.photo--guests{left:350px;top:880px;width:100px;height:100px;background:linear-gradient(160deg,#d9e4ee 0%,#7a8fa3 50%,#2d4a6b 100%)}
.contact{position:absolute;display:flex;align-items:center;gap:8px;font-family:"Oswald",Arial,sans-serif;font-weight:500;font-size:16px;color:var(--white);letter-spacing:.2px}
.contact svg{width:18px;height:18px;flex:none}
.trip{position:absolute;left:0;top:0;width:460px;height:200px}
.trip__title{position:absolute;left:20px;top:18px;font-weight:700;font-size:13px;color:var(--white)}
.trip__text{position:absolute;left:20px;top:36px;width:422px;font-size:11.6px;line-height:1.22;color:var(--white)}
.map{position:absolute;left:0;top:150px;width:460px;height:640px;background:linear-gradient(180deg,#d8e8f4 0%,var(--water) 50%,#c3dbee 100%)}
.service{position:absolute;border-radius:50%;border:6px solid var(--white);display:flex;flex-direction:column;align-items:center;justify-content:center;text-align:center;color:var(--white);box-shadow:0 2px 8px rgba(0,0,0,.25);padding:0 20px}
.service h4{font-family:"Oswald",Arial,sans-serif;font-weight:700;font-size:18px;line-height:1.05;color:var(--gold);margin-bottom:6px;text-transform:uppercase}
.service p{font-size:11.5px;line-height:1.25}
.service--blast{left:272px;top:190px;width:184px;height:184px;background:var(--red)}
.service--half{left:14px;top:338px;width:184px;height:184px;background:var(--blue)}
.service--full{left:246px;top:480px;width:200px;height:200px;background:var(--red)}
.photo--bay{left:0;top:760px;width:460px;height:140px;background:linear-gradient(180deg,#9ec0df 0%,#5c86ad 40%,#2f5f8e 60%,#1e4c7e 100%)}
.badge{position:absolute;left:22px;top:790px;width:62px;height:62px;border-radius:50%;background:var(--white);border:4px solid var(--gold)}
</style>
</head>
<body>

<section class="card card--front">
  <div class="photo photo--hero" role="img" aria-label="Photo from the deck of the sailboat at sunset over the bay"></div>
  <div class="brand"><span class="brand__dot"></span><span class="brand__name">Tidewren</span></div>

  <svg class="abs" style="left:0;top:280px" width="460" height="300" viewBox="0 0 460 300">
    <path d="M0 60 C120 24 260 24 460 50 L460 300 L0 300 Z" fill="var(--white)"/>
    <path d="M0 66 C130 30 270 34 460 60 L460 80 C280 52 130 52 0 88 Z" fill="var(--red)"/>
    <path d="M0 88 C130 52 280 52 460 80 L460 215 C300 205 150 220 0 250 Z" fill="var(--blue)"/>
    <path d="M0 250 C150 220 300 205 460 215 L460 229 C300 221 150 236 0 264 Z" fill="var(--red)"/>
  </svg>
  <p class="headline">Enjoy an amazing experience aboard Tidewren and view San Francisco and the rest of the bay</p>
  <div class="photo photo--circle photo--sails" role="img" aria-label="Photo of the sails and rigging against a blue sky"></div>
  <div class="photo photo--circle photo--moored" role="img" aria-label="Photo of the sailboat moored at the dock"></div>

  <div class="abs section section--modern">
    <h3>Modern</h3>
    <p>Tidewren is completely electric which means no diesel smells, noise or vibration to suffer. New electrics, plumbing, toilets, and deck areas compliment the elegant lines and features of this Harlow Marsh 46 foot cutter rigged sailboat.</p>
  </div>
  <div class="abs section section--entertain">
    <h3>Entertaining</h3>
    <p>Surrounded by the beauty and wonder of the San Francisco Bay you will enjoy the choice of sounds from your source, SkyWave Radio, CD or old school FM! Experience the thrill of sailing Tidewren while we explore Alcatraz and Angel Islands, The Golden Gate and Bay Bridges, the City front or the many other hidden gems. While taking it all in, you and your guests can enjoy refreshments and snacks we provide or even choose to have lunch or dinner at anchor or on a private beach!</p>
  </div>
  <div class="abs section section--safe">
    <h3>Safe</h3>
    <p>We carry aboard everything to make your time aboard safe. Life preservers are of course provided and available for all including kids sizes. We carry the coast guard bulky ones as well as modern self inflating slim comfortable life jackets. Also loaded for every trip is a complete first aid kit, AED, EPIRB, and many other safety items</p>
  </div>

  <svg class="abs" style="left:0;top:870px" width="460" height="130" viewBox="0 0 460 130">
    <path d="M0 40 C150 14 320 20 460 26 L460 130 L0 130 Z" fill="var(--red)"/>
    <path d="M0 50 C150 24 320 30 460 38 L460 130 L0 130 Z" fill="var(--blue)"/>
  </svg>
  <div class="photo photo--circle photo--guests" role="img" aria-label="Photo of guests in life jackets aboard the boat"></div>
  <div class="contact" style="left:22px;top:932px">
    <svg viewBox="0 0 24 24" fill="none" stroke="var(--white)" stroke-width="2"><circle cx="12" cy="12" r="10"/><path d="M8.5 7.5l2 2-1 1.5c.8 1.6 1.9 2.7 3.5 3.5l1.5-1 2 2-1.2 1.5c-3.5-.4-7.3-4.2-7.7-7.7z" fill="var(--white)" stroke="none"/></svg>
    +1 (555) 014 SAIL (7245)
  </div>
  <div class="contact" style="left:22px;top:962px">
    <svg viewBox="0 0 24 24" fill="none" stroke="var(--white)" stroke-width="2"><rect x="2" y="5" width="20" height="14"/><path d="M2 5l10 8 10-8"/></svg>
    Bookings@SailTidewren.com
  </div>
</section>

<section class="card card--back">
  <div class="map" role="img" aria-label="Map of San Francisco Bay showing the three cruise routes"></div>
  <svg class="abs" style="left:0;top:0" width="460" height="230" viewBox="0 0 460 230">
    <path d="M0 0 H460 V160 C330 130 150 150 0 215 Z" fill="var(--blue)"/>
    <path d="M0 215 C150 150 330 130 460 160 L460 170 C330 142 150 162 0 226 Z" fill="var(--red)"/>
  </svg>
  <div class="trip">
    <h2 class="trip__title">THE TRIP</h2>
    <p class="trip__text">When chartering Tidewren, the vessel is yours to direct anywhere within the time you wish to enjoy her. We do have a few old favorites that are always fun that we have listed below. These are just to provide an idea of the possible cruise as every trip takes into account your ideas and natures (tides, weather and currents) will. If your looking for something a little different or to mix it up a bit, let us know and we can make it happen. Our custom trips are simple to arrange and book, we simply ask for a minimum of 3 hours duration.</p>
  </div>

  <svg class="abs" style="left:0;top:150px" width="460" height="640" viewBox="0 0 460 640">
    <path d="M0 250 C120 200 250 215 460 195" stroke="var(--white)" stroke-width="8" fill="none"/>
    <path d="M0 420 C140 380 280 400 460 360" stroke="var(--white)" stroke-width="8" fill="none"/>
  </svg>

  <div class="service service--blast"><h4>2 Hour Blast</h4><p>Could be a sunset sail, an early morning wake up cruise or a blast out into the bay anytime to find peace, fresh air and amazing views.</p></div>
  <div class="service service--half"><h4>½ Day Fun</h4><p>A full morning, afternoon or evening out in the Bay seeing many of the main features and landmarks close to the Bay from the water. Actual duration 4-5 hours</p></div>
  <div class="service service--full"><h4>Full Day<br>Adventure</h4><p>The day includes a complete circuit of the Bay and lunch at anchor. Actual duration 7-8 hours</p></div>

  <div class="photo photo--bay" role="img" aria-label="Photo of the bay with hills and the bridge in the distance"></div>
  <svg class="abs" style="left:0;top:730px" width="460" height="60" viewBox="0 0 460 60">
    <path d="M0 0 C150 50 320 50 460 10 L460 32 C320 62 150 62 0 24 Z" fill="var(--white)"/>
    <path d="M0 24 C150 62 320 62 460 32 L460 40 C320 68 150 68 0 32 Z" fill="var(--red)"/>
  </svg>
  <div class="badge" role="img" aria-label="Certification badge"></div>

  <svg class="abs" style="left:0;top:860px" width="460" height="140" viewBox="0 0 460 140">
    <path d="M0 30 C160 10 320 20 460 18 L460 140 L0 140 Z" fill="var(--blue)"/>
  </svg>
  <div class="contact" style="left:30px;top:902px">
    <svg viewBox="0 0 24 24" fill="none" stroke="var(--white)" stroke-width="2"><circle cx="12" cy="12" r="10"/><path d="M8.5 7.5l2 2-1 1.5c.8 1.6 1.9 2.7 3.5 3.5l1.5-1 2 2-1.2 1.5c-3.5-.4-7.3-4.2-7.7-7.7z" fill="var(--white)" stroke="none"/></svg>
    +1 (555) 014 SAIL (7245)
  </div>
  <div class="contact" style="left:232px;top:902px">
    <svg viewBox="0 0 24 24" fill="none" stroke="var(--white)" stroke-width="2"><rect x="2" y="5" width="20" height="14"/><path d="M2 5l10 8 10-8"/></svg>
    Bookings@SailTidewren.com
  </div>
  <div class="contact" style="left:30px;top:944px">
    <svg viewBox="0 0 24 24" fill="none" stroke="var(--white)" stroke-width="2"><circle cx="12" cy="12" r="10"/><path d="M2 12h20M12 2c3 3 3 17 0 20M12 2c-3 3-3 17 0 20"/></svg>
    www.sailtidewren.com
  </div>
  <div class="contact" style="left:232px;top:944px">
    <svg viewBox="0 0 24 24"><circle cx="12" cy="12" r="10" fill="none" stroke="var(--white)" stroke-width="2"/></svg>
    /tidewrenllc
  </div>
</section>

</body>
</html>
```